Mobile Oil Change company needs a flyer to promote new business

We need a flyer to 1) print & handout and 2) email out to potential customers. We are a mobile oil change company that comes to our customer locations to perform the work instead of customers going to traditional oil change companies. We have a 21 point inspection with our oil change. (21 point inspection details will not be on the flyer). Would like to keep the flyer simple but creative. I'm attaching 1) the write-up we created, 2) our logo (logo color is dark teal on white but other combinations are included if you wanted to propose a different color combination), and 3) additional services we offer. Logo font is Alegreya Sans.
Would like the additional services listed with icons and brief descriptions (similar to attachment) without pricing. Company website for reference is www.brindlefleetcare.com.

Target Market(s)

Companies with many service vehicles such as Oil & Gas service companies, heating and air conditioning companies, utility companies, police departments, etc. Companies that prioritize convenience and maintenance first.

Font styles to use
Sans Serif

Colors
00a990

Requirements
Must have
• Simple but creative design with our logo at top of the flyer. Additional Services (details in document supplied) can be smaller and less prominent than other "main" content listed in the CONTENT document supplied.
Should not have
• Do not use animated character graphics in the flyer and limit (1) stock photos to A small area in the flyer.

```html
<!DOCTYPE html>
<html lang="en">
<head>
<meta charset="utf-8">
<title>Brindle Fleet Care — Hassle Free Oil Changes</title>
<link rel="stylesheet" href="https://fonts.googleapis.com/css2?family=Alegreya+Sans:ital,wght@0,400;0,500;0,700;0,800;1,700&family=Dancing+Script:wght@600&display=swap">
<style>
  :root {
    --teal: #00a990;
    --teal-deep: #0c4f4b;
    --orange: #f28a1d;
    --ink: #1f2b2a;
    --night: #171d1d;
    --grey-ring: #e6e8e8;
    --white: #ffffff;
  }
  * { box-sizing: border-box; margin: 0; padding: 0; }
  html, body { width: 847px; height: 1200px; overflow: hidden; background: var(--white); }
  .flyer {
    position: relative; width: 847px; height: 1200px; overflow: hidden;
    background: var(--white); font-family: "Alegreya Sans", sans-serif; color: var(--ink);
  }
  .backdrop { position: absolute; inset: 0; }
  .hero-art {
    position: absolute; left: 120px; top: 35px; width: 480px; height: 480px; border-radius: 50%;
    border: 12px solid var(--teal);
    background: radial-gradient(circle at 45% 40%, #ffffff 0%, #f2f4f4 55%, #d9dede 100%);
  }
  .brand-halo {
    position: absolute; left: 540px; top: 290px; width: 260px; height: 260px; border-radius: 50%;
    background: var(--grey-ring);
  }
  .brand-badge {
    position: absolute; left: 500px; top: 332px; width: 250px; height: 250px; border-radius: 50%;
    background: var(--teal-deep); display: flex; flex-direction: column; align-items: center; justify-content: center;
    color: var(--white); font-weight: 700; text-align: center; line-height: 1;
  }
  .brand-badge .name-main { font-size: 44px; letter-spacing: 1px; }
  .brand-badge .name-sub { font-size: 19px; letter-spacing: 3px; margin-top: 8px; }
  .headline { position: absolute; left: 0; right: 0; top: 580px; text-align: center; font-weight: 400; }
  .headline .script { display: block; font-family: "Dancing Script", cursive; font-weight: 600; color: var(--teal); font-size: 60px; line-height: 1; margin-left: 40px; }
  .headline .main { display: block; font-size: 52px; font-weight: 500; color: var(--teal); line-height: 1; margin-top: 2px; }
  .headline .main strong { color: var(--orange); font-weight: 800; }
  .headline-rule { position: absolute; left: 290px; width: 330px; top: 708px; height: 1px; background: #b9c2c1; }
  .process-intro { position: absolute; left: 0; right: 0; top: 718px; text-align: center; }
  .process-intro h2 { font-size: 28px; font-weight: 700; color: var(--ink); }
  .process-intro p { font-size: 17px; color: var(--teal); margin-top: 2px; }
  .process-intro p strong { color: var(--orange); font-weight: 700; }
  .step { position: absolute; display: flex; align-items: center; gap: 16px; width: 320px; }
  .step-icon { position: relative; flex: 0 0 58px; width: 58px; height: 58px; border-radius: 50%; background: var(--night); display: flex; align-items: center; justify-content: center; }
  .step-number { position: absolute; left: -2px; top: -4px; width: 18px; height: 18px; border-radius: 50%; background: var(--white); border: 1px solid #999; font-size: 11px; font-weight: 700; display: flex; align-items: center; justify-content: center; }
  .step-text { font-style: italic; font-weight: 700; font-size: 20px; line-height: 1.15; color: var(--ink); }
  .step-1 { left: 90px; top: 800px; }
  .step-2 { left: 90px; top: 876px; }
  .step-3 { left: 90px; top: 950px; }
  .step-4 { left: 455px; top: 800px; }
  .step-5 { left: 455px; top: 876px; }
  .perks { position: absolute; left: 110px; top: 1026px; list-style: none; color: var(--white); font-size: 17px; }
  .perks li { display: flex; align-items: center; gap: 14px; height: 24px; }
  .contact { position: absolute; left: 28px; top: 1128px; }
  .contact .call { font-size: 30px; color: var(--teal); font-weight: 500; line-height: 1.1; }
  .contact .call strong { color: var(--orange); font-weight: 700; }
  .contact .mail { font-size: 17px; color: var(--teal); }
  .contact .mail strong { color: var(--orange); font-weight: 700; }
  .website { position: absolute; right: 36px; top: 1147px; font-size: 16px; color: var(--white); }
</style>
</head>
<body>
<main class="flyer">
  <svg class="backdrop" width="847" height="1200" viewBox="0 0 847 1200" aria-hidden="true">
    <polygon points="0,0 520,0 0,520" fill="var(--teal-deep)"/>
    <polygon points="0,520 280,640 0,680" fill="var(--teal-deep)"/>
    <polygon points="0,520 300,650 300,660 0,532" fill="var(--teal)"/>
    <polygon points="690,0 847,0 847,500 520,500" fill="var(--teal-deep)"/>
    <polygon points="847,0 847,40 610,0" fill="var(--teal)"/>
    <polygon points="847,878 847,1200 470,1200 590,1098 700,1012" fill="var(--teal-deep)"/>
    <polygon points="0,1012 740,1012 650,1098 0,1098" fill="var(--teal)"/>
    <polygon points="740,1012 847,1012 847,1098 650,1098" fill="var(--night)"/>
  </svg>

  <div class="hero-art" role="img" aria-label="Illustration of a mechanic working under the raised hood of a car"></div>

  <div class="brand-halo"></div>
  <div class="brand-badge">
    <span class="name-main">BRINDLE</span>
    <span class="name-sub">FLEET CARE</span>
  </div>

  <h1 class="headline">
    <span class="script">Hassle Free</span>
    <span class="main"><strong>Oil Changes</strong> on your terms</span>
  </h1>
  <div class="headline-rule"></div>

  <section class="process-intro">
    <h2>Our simple 5-step process</h2>
    <p>lets you schedule an appointment and get service to <strong>save time &amp; money:</strong></p>
  </section>

  <div class="step step-1">
    <div class="step-icon"><span class="step-number">1</span>
      <svg width="30" height="30" viewBox="0 0 30 30"><rect x="4" y="7" width="22" height="19" rx="2" fill="none" stroke="var(--orange)" stroke-width="2.5"/><line x1="4" y1="12" x2="26" y2="12" stroke="var(--orange)" stroke-width="2.5"/><line x1="10" y1="4" x2="10" y2="9" stroke="var(--orange)" stroke-width="2.5"/><line x1="20" y1="4" x2="20" y2="9" stroke="var(--orange)" stroke-width="2.5"/></svg>
    </div>
    <p class="step-text">Call or email us to schedule service</p>
  </div>
  <div class="step step-2">
    <div class="step-icon"><span class="step-number">2</span>
      <svg width="30" height="30" viewBox="0 0 30 30"><path d="M20 4a6 6 0 0 0-5.6 8.2L5 21.6 8.4 25l9.4-9.4A6 6 0 0 0 26 10l-3.6 3.6-3.6-1-1-3.6z" fill="var(--orange)"/></svg>
    </div>
    <p class="step-text">Our highly trained technicians come to you for service</p>
  </div>
  <div class="step step-3">
    <div class="step-icon"><span class="step-number">3</span>
      <svg width="32" height="30" viewBox="0 0 32 30"><path d="M5 17l3-8h16l3 8v7H5z" fill="var(--orange)"/><circle cx="10" cy="24" r="3" fill="var(--night)"/><circle cx="22" cy="24" r="3" fill="var(--night)"/><rect x="10" y="11" width="12" height="5" fill="var(--night)"/></svg>
    </div>
    <p class="step-text">Service is performed quickly on your vehicle</p>
  </div>
  <div class="step step-4">
    <div class="step-icon"><span class="step-number">4</span>
      <svg width="30" height="30" viewBox="0 0 30 30"><rect x="3" y="8" width="24" height="16" rx="2" fill="var(--orange)"/><rect x="3" y="12" width="24" height="3" fill="var(--night)"/><rect x="19" y="18" width="5" height="3" fill="var(--night)"/></svg>
    </div>
    <p class="step-text">Pay agreed-upon pricing and receipt is emailed to you</p>
  </div>
  <div class="step step-5">
    <div class="step-icon"><span class="step-number">5</span>
      <svg width="30" height="30" viewBox="0 0 30 30"><path d="M15 4c-5 0-8 3.5-8 8v6l-3 4h22l-3-4v-6c0-4.5-3-8-8-8z" fill="var(--orange)"/><circle cx="15" cy="25" r="2.5" fill="var(--orange)"/></svg>
    </div>
    <p class="step-text">Services performed are tracked electronically and reminders created</p>
  </div>

  <ul class="perks">
    <li><svg width="16" height="16" viewBox="0 0 16 16"><circle cx="8" cy="8" r="7" fill="none" stroke="#fff" stroke-width="1.5"/><path d="M4.5 8.2l2.3 2.3 4.7-4.8" fill="none" stroke="#fff" stroke-width="1.6"/></svg>High quality synthetic oil used is best suited for commercial vehicles</li>
    <li><svg width="16" height="16" viewBox="0 0 16 16"><circle cx="8" cy="8" r="7" fill="none" stroke="#fff" stroke-width="1.5"/><path d="M4.5 8.2l2.3 2.3 4.7-4.8" fill="none" stroke="#fff" stroke-width="1.6"/></svg>Service includes a 21-point inspection</li>
    <li><svg width="16" height="16" viewBox="0 0 16 16"><circle cx="8" cy="8" r="7" fill="none" stroke="#fff" stroke-width="1.5"/><path d="M4.5 8.2l2.3 2.3 4.7-4.8" fill="none" stroke="#fff" stroke-width="1.6"/></svg>Additional services are available</li>
  </ul>

  <footer class="contact">
    <p class="call">Call Now @ <strong>(833) 555-0142</strong></p>
    <p class="mail">or Email us at <strong>sales@brindlefleetcare.com</strong></p>
  </footer>
  <p class="website">www.brindlefleetcare.com</p>
</main>
</body>
</html>
```